Informational Site for Advanced Chemistry R&D

The company develops oxidation chemistry for air, water, fuel pollution controls. The site has been prototyped at www.velmirlab.net. Take a look. Now, the task is to design it for eye-catching beauty with use of color, on-page scroll-driven color transition and parallax effects. Should capture the themes: high technology, wow it's beautiful, modern, uncluttered, clean urban environment.

Target Market(s)

China Environmentally Conscious Government and Industry,

Industry/Entity Type

It Company

Number of Pages Required

3 page

Font styles to use
Sans Serif

Requirements
Must have
• Parallax effects, desktop compatible, Rich, Modern, Simple, Graphic
Nice to have
• Mobile Phone Compatible
Should not have
• Flash, or anything that is slow to load or requires high bandwidth

```html
<!DOCTYPE html>
<html lang="en">
<head>
<meta charset="utf-8">
<title>Velmir — Advanced Oxidation Science</title>
<link rel="stylesheet" href="https://fonts.googleapis.com/css2?family=Open+Sans:wght@400;600;700&family=Oswald:wght@400;500&family=Montserrat:wght@600;700&display=swap">
<style>
:root{
  --teal:#3dbdb4;
  --teal-dark:#2ea79e;
  --blue:#1b74bd;
  --footer:#1f6fb3;
  --orange:#f6ad2d;
  --rust:#d9622c;
  --green:#8dbb2a;
  --ink:#2d2d2d;
  --grey:#eeeeee;
  --white:#ffffff;
  --muted:#666;
}
*{box-sizing:border-box;margin:0;padding:0}
html,body{width:1200px;height:3956px;overflow:hidden}
body{position:relative;background:var(--white);font-family:"Open Sans",Arial,sans-serif;color:var(--ink)}
.abs{position:absolute}

/* header */
.site-header{left:0;top:0;width:1200px;height:105px;background:var(--teal)}
.brand-tab{left:0;top:0;width:300px;height:105px}
.brand{left:40px;top:22px;display:flex;flex-direction:column;align-items:center;gap:4px}
.brand-dot{width:38px;height:38px;border-radius:50%;background:var(--teal)}
.brand-name{font-weight:700;font-size:20px;color:var(--teal)}
.main-nav{left:0;top:0;width:1200px;height:105px}
.main-nav a{position:absolute;top:42px;color:var(--white);font-size:17px;text-decoration:none;letter-spacing:.5px}

/* hero */
.hero{left:0;top:105px;width:1200px;height:586px;background:linear-gradient(180deg,#2f6fae 0%,#6ea7d6 30%,#d9ebf6 55%,#b9d860 68%,#7fb52a 82%,#5c9a1c 100%)}
.hero-title{left:0;top:340px;width:1200px;text-align:center;font-family:"Montserrat",sans-serif;font-weight:700;font-size:44px;letter-spacing:10px;color:#111}
.hero-sub{left:0;top:392px;width:1200px;text-align:center;font-size:29px;letter-spacing:2px;color:#1c1c1c}
.hero-arrow{top:378px;width:30px;height:40px}

/* intro */
.intro{left:0;top:691px;width:541px;height:259px;background:var(--white);text-align:center}
.intro-lead{position:absolute;left:0;top:28px;width:541px;font-family:"Oswald",sans-serif;font-size:20px;line-height:25px;color:#111;text-transform:uppercase}
.intro-brand{position:absolute;left:0;top:92px;width:541px;display:flex;flex-direction:column;align-items:center;gap:6px}
.intro-brand .brand-dot{width:46px;height:46px}
.intro-brand .brand-name{font-size:24px}
.intro-link{position:absolute;left:103px;top:207px;width:318px;height:44px;border:1px solid #bbb;font-size:13px;line-height:42px;color:#333}
.card{top:701px;height:249px;padding:22px 26px;color:var(--white)}
.card h3{font-family:"Oswald",sans-serif;font-weight:400;font-size:27px;display:flex;align-items:center;gap:10px}
.card p{font-size:13px;line-height:20px;margin-top:14px}
.card .date{margin-top:10px}
.card .dots{position:absolute;left:0;bottom:28px;width:100%;display:flex;justify-content:center;gap:8px}
.card .dots i{width:8px;height:8px;border-radius:50%;background:rgba(255,255,255,.55)}
.card .dots i:first-child{background:var(--white)}
.card .more{position:absolute;right:14px;bottom:14px;background:#1d3f56;font-size:11px;padding:4px 10px}
.card-events{left:543px;width:288px;background:var(--teal)}
.card-news{left:833px;width:291px;background:var(--blue)}

/* section heading */
.section-title{left:0;width:1200px;text-align:center;font-family:"Montserrat",sans-serif;font-weight:700;font-size:32px;letter-spacing:1px;color:#2a2a2a}
.section-rule{left:570px;width:60px;height:3px;background:var(--teal)}

/* solutions */
.band{left:0;width:1200px;height:444px}
.band-water{top:1129px;background:linear-gradient(135deg,#1f5e98 0%,#3f8cc4 45%,#9dbfd6 70%,#2d6a9a 100%)}
.band-diesel{top:1619px;background:linear-gradient(90deg,#e6e1d6 0%,#cfc6b7 40%,#2f7fcf 55%,#5aa2e6 100%)}
.band-coal{top:2102px;background:linear-gradient(180deg,#1f5ea8 0%,#4a8cd0 40%,#b58a5d 75%,#6b4a2f 100%)}
.band-voc{top:2587px;background:linear-gradient(180deg,#5585b6 0%,#b3c6d6 45%,#e9eef2 75%,#4a4f4c 100%)}
.panel{padding:28px 28px;color:var(--white)}
.panel h2{font-family:"Oswald",sans-serif;font-weight:500;font-size:37px;line-height:40px;text-transform:uppercase}
.panel p{font-size:13.5px;line-height:22px;margin-top:18px}
.panel .btn{display:inline-block;margin-top:24px;border:1px solid rgba(255,255,255,.85);font-size:13px;padding:12px 20px}
.panel-water{left:37px;top:1110px;width:298px;height:438px;background:var(--orange)}
.panel-diesel{left:868px;top:1598px;width:295px;height:433px;background:var(--teal)}
.panel-coal{left:37px;top:2086px;width:298px;height:372px;background:var(--rust)}
.panel-voc{left:873px;top:2571px;width:290px;height:356px;background:var(--green)}

/* posts */
.posts{left:0;top:3033px;width:1200px;height:638px;background:var(--grey)}
.post{top:3191px;width:332px}
.post-img{width:332px;height:316px;position:relative}
.post h4{font-size:15px;font-weight:600;line-height:22px;margin-top:30px;color:#333;max-width:300px}
.post .meta{font-size:12px;margin-top:14px;color:var(--muted)}
.post .meta span{color:var(--teal)}
.post-btn{position:absolute;left:0;top:160px;width:126px;height:44px;border:1px solid rgba(255,255,255,.9);color:var(--white);font-size:13px;text-align:center;line-height:42px}

/* footer */
.site-footer{left:0;top:3671px;width:1200px;height:285px;background:var(--footer);color:var(--white)}
.foot-col{top:68px}
.foot-col h5{font-size:15px;font-weight:700;letter-spacing:.5px;text-transform:uppercase}
.foot-col .links{display:grid;grid-template-columns:110px 80px;row-gap:6px;margin-top:24px;font-size:12px}
.foot-col p{font-size:12px;line-height:24px;margin-top:18px}
.foot-col .soft{color:#8fd0f0}
.socials{display:flex;gap:8px;margin-top:10px}
.socials i{width:28px;height:28px;border-radius:50%;border:2px solid #5fc4e8}
.subscribe{display:flex;align-items:center;gap:12px;margin-top:14px}
.subscribe span{width:190px;height:40px;border-radius:20px;background:var(--white);color:#999;font-size:12px;line-height:40px;padding-left:16px}
.foot-rule{left:74px;top:226px;width:1052px;height:1px;background:rgba(255,255,255,.3)}
.copyright{left:74px;top:246px;font-size:13px}
.copyright span{color:#8fd0f0}
</style>
</head>
<body>

<header class="site-header abs">
  <svg class="brand-tab abs" viewBox="0 0 300 105"><polygon points="0,0 262,0 300,52 262,105 0,105" fill="#fff"/></svg>
  <div class="brand abs"><span class="brand-dot"></span><span class="brand-name">Velmir</span></div>
  <nav class="main-nav abs">
    <a style="left:417px">HOME</a>
    <a style="left:542px">WATER</a>
    <a style="left:672px">DIESEL</a>
    <a style="left:806px">COAL</a>
    <a style="left:926px">VOC</a>
    <a style="left:1033px">ABOUT</a>
  </nav>
</header>

<section class="hero abs" role="img" aria-label="Photograph of a green wheat field under a bright blue sky with clouds">
</section>
<svg class="hero-arrow abs" style="left:36px" viewBox="0 0 30 40"><polyline points="22,4 8,20 22,36" fill="none" stroke="#fff" stroke-width="5" opacity=".8"/></svg>
<svg class="hero-arrow abs" style="left:1134px" viewBox="0 0 30 40"><polyline points="8,4 22,20 8,36" fill="none" stroke="#fff" stroke-width="5" opacity=".8"/></svg>
<h1 class="hero-title abs">ADVANCED OXIDATION SCIENCE</h1>
<p class="hero-sub abs">FOR ENVIRONMENTAL POLLUTION MANAGEMENT</p>

<section class="intro abs">
  <p class="intro-lead">Environmental pollution control solutions<br>employing nature's most reactive free radical</p>
  <div class="intro-brand"><span class="brand-dot"></span><span class="brand-name">Velmir</span></div>
  <div class="intro-link">LEARN ABOUT ADVANCED OXIDATION CHEMISTRY</div>
</section>

<article class="card card-events abs">
  <h3><svg width="22" height="22" viewBox="0 0 22 22"><rect x="2" y="4" width="18" height="16" fill="none" stroke="#fff" stroke-width="2"/><line x1="2" y1="9" x2="20" y2="9" stroke="#fff" stroke-width="2"/><line x1="7" y1="1" x2="7" y2="6" stroke="#fff" stroke-width="2"/><line x1="15" y1="1" x2="15" y2="6" stroke="#fff" stroke-width="2"/></svg>Events</h3>
  <p>Lorem ipsum dolor sit amet,</p>
  <p class="date">01 Jan 2016</p>
  <p class="date">Suspendisse nec felis consectetur,<br>vulputate nisl quis, porttitor turpis.<br>Suspendisse nec felis consectetur.</p>
  <div class="dots"><i></i><i></i><i></i></div>
  <span class="more">More</span>
</article>

<article class="card card-news abs">
  <h3><svg width="22" height="22" viewBox="0 0 22 22"><rect x="2" y="3" width="18" height="16" fill="none" stroke="#fff" stroke-width="2"/><line x1="6" y1="8" x2="16" y2="8" stroke="#fff" stroke-width="2"/><line x1="6" y1="13" x2="16" y2="13" stroke="#fff" stroke-width="2"/></svg>News</h3>
  <p>Lorem ipsum dolor sit amet,</p>
  <p class="date">01 Jan 2016</p>
  <p class="date">Suspendisse nec felis consectetur,<br>vulputate nisl quis, porttitor turpis.<br>Suspendisse nec felis consectetur.</p>
  <div class="dots"><i></i><i></i><i></i></div>
  <span class="more">More</span>
</article>

<h2 class="section-title abs" style="top:1012px">SOLUTIONS FOR</h2>
<div class="section-rule abs" style="top:1062px"></div>

<div class="band band-water abs" role="img" aria-label="Photograph of a circular wastewater treatment basin with a walkway over blue water"></div>
<article class="panel panel-water abs">
  <h2>Wastewater</h2>
  <p>Lorem ipsum dolor sit amet, consectetur adipiscing elit, sed do eiusmod tempor incididunt ut labore et dolore magna aliqua. Ut enim ad minim veniam, quis nostrud exercitation ullamco laboris nisi ut aliquip ex ea commodo consequat.</p>
  <span class="btn">LEARN MORE</span>
</article>

<div class="band band-diesel abs" role="img" aria-label="Photograph of large white spherical fuel storage tanks with stairways against a blue sky"></div>
<article class="panel panel-diesel abs">
  <h2>Diesel Fuel</h2>
  <p>Lorem ipsum dolor sit amet, consectetur adipiscing elit, sed do eiusmod tempor incididunt ut labore et dolore magna aliqua. Ut enim ad minim veniam, quis nostrud exercitation ullamco laboris nisi ut aliquip ex ea commodo consequat.</p>
  <span class="btn">LEARN MORE</span>
</article>

<div class="band band-coal abs" role="img" aria-label="Photograph of power station cooling towers releasing steam under a blue sky"></div>
<article class="panel panel-coal abs">
  <h2>Coal Flue Gas</h2>
  <p>Lorem ipsum dolor sit amet, consectetur adipiscing elit, sed do eiusmod tempor incididunt ut labore et dolore magna aliqua. Ut enim ad minim veniam, quis nostrud exercitation ullamco laboris nisi ut aliquip ex ea commodo consequat.</p>
  <span class="btn">LEARN MORE</span>
</article>

<div class="band band-voc abs" role="img" aria-label="Photograph of industrial smokestacks emitting white smoke over a hazy landscape"></div>
<article class="panel panel-voc abs">
  <h2>Volatile<br>Organics</h2>
  <p>Lorem ipsum dolor sit amet, consectetur adipiscing elit, sed do eiusmod tempor incididunt ut labore et dolore magna aliqua. Ut enim ad minim veniam, quis nostrud exercitation ullamco laboris nisi ut aliquip ex ea commodo consequat.</p>
  <span class="btn">LEARN MORE</span>
</article>

<section class="posts abs"></section>
<h2 class="section-title abs" style="top:3076px">LATEST POSTS</h2>
<div class="section-rule abs" style="top:3126px"></div>

<article class="post abs" style="left:74px">
  <div class="post-img" role="img" aria-label="Photograph of cooling towers under a teal-tinted sky" style="background:linear-gradient(180deg,#4fc7c0 0%,#3db3ad 60%,#2d8f8a 100%)">
    <span class="post-btn">LEARN MORE</span>
    <svg class="abs" style="left:146px;top:160px" width="40" height="40" viewBox="0 0 40 40"><line x1="20" y1="4" x2="20" y2="36" stroke="#fff" stroke-width="3"/><line x1="4" y1="20" x2="36" y2="20" stroke="#fff" stroke-width="3"/></svg>
  </div>
  <h4>Sed ut perspiciatis unde omnis iste<br>natus error sit voluptatem accusa</h4>
  <p class="meta"><span>John Doe</span> | on 11th January, 2016</p>
</article>

<article class="post abs" style="left:435px">
  <div class="post-img" role="img" aria-label="Photograph of the sun shining over a green field under a blue sky" style="background:linear-gradient(180deg,#1f6fc4 0%,#7ab6e8 45%,#e8f2da 60%,#8cc63f 75%,#4f8f1f 100%)"></div>
  <h4>Sed ut perspiciatis unde omnis iste<br>natus error sit voluptatem accusa</h4>
  <p class="meta"><span>John Doe</span> | on 11th January, 2016</p>
</article>

<article class="post abs" style="left:794px">
  <div class="post-img" role="img" aria-label="Photograph of two engineers in hard hats inspecting industrial pipework" style="background:linear-gradient(135deg,#b9d2e6 0%,#dfe7ec 45%,#8a9aa6 75%,#2f3b4a 100%)"></div>
  <h4>Sed ut perspiciatis unde omnis iste<br>natus error sit voluptatem accusa</h4>
  <p class="meta"><span>John Doe</span> | on 11th January, 2016</p>
</article>

<footer class="site-footer abs">
  <div class="foot-col abs" style="left:74px">
    <h5>Company</h5>
    <div class="links"><span>HOME</span><span>COAL</span><span>WATER</span><span>VOC</span><span>DIESEL</span><span>ABOUT</span></div>
  </div>
  <div class="foot-col abs" style="left:343px">
    <h5>Come and Visit</h5>
    <p>Your Company LTD.<br>Street Name, 000000, City Name</p>
    <p class="soft" style="margin-top:4px">View on City Map</p>
  </div>
  <div class="foot-col abs" style="left:612px">
    <h5>Get in Touch</h5>
    <p>1-000-000-0000<br><span class="soft">info@yourdomain.com</span></p>
    <div class="socials"><i></i><i></i></div>
  </div>
  <div class="foot-col abs" style="left:883px">
    <h5>Stay Informed</h5>
    <p>Get news, views, insight and events</p>
    <div class="subscribe"><span>Enter email address</span>
      <svg width="40" height="40" viewBox="0 0 40 40"><circle cx="20" cy="20" r="18" fill="none" stroke="#5fc4e8" stroke-width="2.5"/><polyline points="16,12 24,20 16,28" fill="none" stroke="#5fc4e8" stroke-width="3"/></svg>
    </div>
  </div>
  <div class="foot-rule abs"></div>
  <p class="copyright abs">© 2016 <span>Velmir Lab Corporation</span>. All rights reserved.</p>
</footer>

</body>
</html>
```